Business Card That Looks Like a Sports Card

Want it to look like a sports trading card. That front should have a baseball player. The back will list our contact info and website info etc.

Contact Information for Business Card

www.ridgecrestathletics.example
visitRCX.example
Email: marcus@ridgecrestathletics.example

Colors

Designer to choose colors to be used in the design.

Requirements
Must have
• Use our current logo and color scheme. Must look like a sports trading card.

```html
<!DOCTYPE html>
<html lang="en">
<head>
<meta charset="utf-8">
<title>Ridgecrest Athletics – Business Card</title>
<link rel="stylesheet" href="https://fonts.googleapis.com/css2?family=Russo+One&family=Saira+Condensed:wght@500&display=swap">
<style>
  :root {
    --page: #3a3b3d;
    --card: #1f2021;
    --card-edge: #2a2b2d;
    --teal: #13b595;
    --navy: #1b2a4a;
    --grey: #c9cdd2;
    --white: #f2f3f4;
  }
  * { box-sizing: border-box; margin: 0; padding: 0; }
  html, body { width: 1200px; height: 900px; overflow: hidden; }
  body { background: var(--page); position: relative; }

  .card {
    position: absolute;
    left: 200px;
    width: 800px;
    height: 410px;
    background: linear-gradient(135deg, var(--card-edge), var(--card) 60%);
    border-radius: 22px;
    overflow: hidden;
  }
  .card::after {
    content: "";
    position: absolute;
    left: 0; right: 0; bottom: 0;
    height: 16px;
    background: var(--teal);
  }
  .card--front { top: 30px; }
  .card--back { top: 460px; }

  .player-art {
    position: absolute;
    left: 70px; top: 30px;
    width: 330px; height: 340px;
    border-radius: 16px;
    background: radial-gradient(ellipse at 45% 45%, #c9cdd2 0%, #8e959e 45%, #1b2a4a 100%);
    opacity: .85;
  }

  .brand {
    position: absolute;
    display: flex;
    align-items: center;
    gap: 14px;
    font-family: "Russo One", sans-serif;
    color: var(--teal);
    text-transform: uppercase;
    line-height: 1.05;
  }
  .brand__dot {
    width: 26px; height: 26px;
    border-radius: 50%;
    background: var(--teal);
    flex: none;
  }
  .card--front .brand { left: 450px; top: 150px; font-size: 38px; }
  .card--back .brand { left: 60px; top: 150px; font-size: 38px; }

  .person {
    position: absolute;
    right: 62px; top: 52px;
    text-align: right;
    font-family: "Russo One", sans-serif;
    text-transform: uppercase;
  }
  .person__name { color: var(--teal); font-size: 38px; letter-spacing: 4px; }
  .person__title { color: var(--white); font-size: 20px; letter-spacing: 3px; margin-top: 6px; }
  .accent-bar {
    position: absolute;
    right: 0; top: 70px;
    width: 18px; height: 76px;
    background: var(--teal);
  }

  .contact {
    position: absolute;
    right: 40px; bottom: 50px;
    list-style: none;
    font-family: "Saira Condensed", sans-serif;
    font-weight: 500;
    color: var(--white);
    font-size: 26px;
    letter-spacing: 2.5px;
    text-transform: uppercase;
  }
  .contact li {
    display: flex;
    justify-content: flex-end;
    align-items: center;
    gap: 16px;
    height: 44px;
  }
  .contact svg { width: 24px; height: 24px; flex: none; }
</style>
</head>
<body>

  <section class="card card--front" aria-label="Card front">
    <div class="player-art" role="img" aria-label="Illustration of a baseball player swinging a bat"></div>
    <div class="brand"><span class="brand__dot"></span><span>Ridgecrest<br>Athletics</span></div>
  </section>

  <section class="card card--back" aria-label="Card back">
    <div class="brand"><span class="brand__dot"></span><span>Ridgecrest<br>Athletics</span></div>

    <div class="person">
      <p class="person__name">Marcus Bennett</p>
      <p class="person__title">Director</p>
    </div>
    <span class="accent-bar"></span>

    <ul class="contact">
      <li>(555) 014-2290
        <svg viewBox="0 0 24 24" fill="none" stroke="#13b595" stroke-width="2" stroke-linecap="round" stroke-linejoin="round"><path d="M6 3h3l2 5-2 1.5a11 11 0 0 0 5.5 5.5L16 13l5 2v3a2 2 0 0 1-2 2A16 16 0 0 1 4 5a2 2 0 0 1 2-2z"/></svg>
      </li>
      <li>marcus@ridgecrestathletics.example
        <svg viewBox="0 0 24 24" fill="none" stroke="#13b595" stroke-width="2" stroke-linejoin="round"><rect x="3" y="5" width="18" height="14" rx="1"/><path d="M3 6l9 7 9-7"/></svg>
      </li>
      <li>www.ridgecrestathletics.example
        <svg viewBox="0 0 24 24" fill="none" stroke="#13b595" stroke-width="1.8"><circle cx="12" cy="12" r="9"/><ellipse cx="12" cy="12" rx="4" ry="9"/><path d="M3 12h18M5 7h14M5 17h14"/></svg>
      </li>
      <li>www.visitRCX.example
        <svg viewBox="0 0 24 24" fill="none" stroke="#13b595" stroke-width="1.8"><circle cx="12" cy="12" r="9"/><ellipse cx="12" cy="12" rx="4" ry="9"/><path d="M3 12h18M5 7h14M5 17h14"/></svg>
      </li>
    </ul>
  </section>

</body>
</html>
```